Local snack brand needs a WordPress theme design

We need a custom WordPress theme for a new Australian snack company called Crunchwell. Based in Palmera Bay, we create functional food snacks using local bananas and other produce. The theme should reflect our community-first philosophy and local roots, featuring an aerial banner of the region’s banana plantations and images of growers harvesting bananas.
The design should include layouts for:
1. Bio pages (profile photo and blurb)
2. Product pages (packaging, nutrition information panel, ingredients, 3. product description, health claim badges like “source of fibre” and “good source of potassium,” and awards)
4. Where to Buy page (interactive map, market stall imagery)
5. Blog posts (feature image, paragraph, quotes)
The final theme should use Crunchwell’s vector logo in the header (without text), and Crunchwell name (in brand font) in the footer. Should be modern, responsive design (mobile first). It should have a grass roots feel, be clean and feel good, leverage the brand colours, but still feel professional (to reflect a horticulturist and nutritionist), and be flexible for future updates. The successful design needs to be delivered as an installable theme in ZIP archive.
Please visit our website and read our pages to get a feel for "us". See https://crunchwell-example.au/
Updates
1 week extension for the 3 finalists to respond to feedback and make their final submissions before awarding 1st, 2nd and 3rd.
Target Market(s)
Local, health-conscious, athletes, busy parents, active minds
Industry/Entity Type
Food wholesaler, health & nutrition, agribusiness / local produce
Coding
Coded - Design and coding required
Font styles to use
Other font styles liked:
- Galano Grotesque Bold

```html
<!DOCTYPE html>
<html lang="en">
<head>
<meta charset="utf-8">
<title>Crunchwell — Rescued Produce. Real Nutrition. Good Energy</title>
<link href="https://fonts.googleapis.com/css2?family=Outfit:wght@500;600;700;800&family=Poppins:wght@400;500;600&display=swap" rel="stylesheet">
<style>
:root{
  --green:#5b9a2e;
  --green-bright:#6fae33;
  --green-soft:#e4ecd8;
  --green-pale:#a9cc8a;
  --ink:#1b1b1b;
  --text:#3c3c3c;
  --muted:#6a6a6a;
  --grey-band:#ebebeb;
  --white:#ffffff;
  --footer:#141414;
  --head:'Outfit',sans-serif;
  --body:'Poppins',sans-serif;
}
*{box-sizing:border-box;margin:0;padding:0}
html,body{width:1200px;height:4021px;overflow:hidden}
body{position:relative;background:var(--white);font-family:var(--body);color:var(--text)}
.abs{position:absolute}
a{color:inherit;text-decoration:none}
.btn{position:absolute;display:flex;align-items:center;justify-content:center;gap:8px;border-radius:30px;font-family:var(--body);font-weight:600;font-size:11.5px;height:38px}
.btn-solid{background:var(--green);color:var(--white)}
.btn-outline{border:1.5px solid var(--green);color:var(--green);background:transparent}
.btn-white{background:var(--white);color:var(--green)}
.btn-ghost{border:1.5px solid var(--white);color:var(--white)}

/* header */
.site-header{position:absolute;top:0;left:0;width:1200px;height:47px;background:var(--white);z-index:5}
.nav{position:absolute;top:16px;font-size:11.5px;font-weight:500;color:var(--ink);display:flex;gap:31px}
.nav-left{left:121px}
.nav-right{left:732px}
.logo-notch{position:absolute;left:512px;top:-90px;width:176px;height:176px;border-radius:50%;background:var(--white);z-index:5}
.logo-mark{position:absolute;left:586px;top:8px;width:28px;height:28px;border-radius:50%;background:var(--green);z-index:6}
.logo-name{position:absolute;left:0;width:1200px;top:50px;text-align:center;font-family:var(--head);font-weight:700;font-size:14px;color:var(--ink);z-index:6;letter-spacing:.5px}
.account{position:absolute;left:925px;top:13px;width:22px;height:22px;border-radius:50%;border:1.5px solid var(--green)}
.account::after{content:"";position:absolute;left:6px;top:4px;width:7px;height:7px;border-radius:50%;background:var(--green)}

/* hero */
.hero-media{position:absolute;top:0;left:0;width:1200px;height:660px;background:radial-gradient(ellipse at 50% 45%,#2a2d2b 0%,#1c1f1e 60%,#151716 100%)}
.hero-title{position:absolute;top:255px;left:0;width:1200px;text-align:center;font-family:var(--head);font-weight:700;font-size:57px;line-height:67px;color:var(--white)}
.hero-title .accent{color:var(--green-bright)}
.hero-sub{position:absolute;top:393px;width:1200px;text-align:center;color:var(--white);font-size:11px}

/* intro */
.eyebrow{position:absolute;left:122px;top:737px;font-size:15px;color:var(--green);display:flex;align-items:center;gap:8px}
.eyebrow::after{content:"";width:34px;height:1.5px;background:var(--green)}
.intro-title{position:absolute;left:122px;top:766px;font-family:var(--head);font-weight:700;font-size:37px;line-height:46px;color:var(--ink)}
.intro-text{position:absolute;left:572px;top:722px;width:500px;font-size:15.5px;line-height:30px;color:var(--ink)}
.deco-mark{position:absolute;left:945px;top:650px;width:255px;height:340px;background:radial-gradient(circle at 60% 45%,#f1f3ee 0 45%,transparent 46%)}

/* snacks */
.snacks{position:absolute;top:988px;left:0;width:1200px;height:604px;background:var(--grey-band)}
.section-title{position:absolute;left:0;width:1200px;text-align:center;font-family:var(--head);font-weight:700;font-size:37px;color:var(--ink)}
.card{position:absolute;top:1110px;width:305px;height:349px;background:var(--green-soft);border:5px solid #f5f6f3;box-shadow:0 3px 10px rgba(0,0,0,.08)}
.card-media{position:absolute;left:0;top:0;width:100%;height:203px;background:linear-gradient(180deg,#f2f4ef 0%,#d9e6c9 100%)}
.pack{position:absolute;left:97px;top:20px;width:100px;height:168px;border-radius:8px;background:linear-gradient(180deg,#a6d23c,#8dbd2b)}
.card h3{position:absolute;left:19px;top:222px;font-family:var(--head);font-weight:600;font-size:19px;color:var(--ink)}
.card .desc{position:absolute;left:19px;top:256px;font-size:10.5px;color:var(--ink)}
.card .tags{position:absolute;left:19px;top:275px;font-size:10.5px;color:var(--ink)}
.card .more{position:absolute;left:19px;top:307px;font-size:11.5px;font-weight:600;color:var(--green)}
.arrow-circle{position:absolute;width:18px;height:18px;border-radius:50%;border:1.3px solid var(--ink)}

/* why */
.why-emblem{position:absolute;left:428px;top:1724px;width:344px;height:344px;border-radius:50%;background:var(--green-pale)}
.why-emblem::after{content:"";position:absolute;left:18px;top:18px;width:308px;height:308px;border-radius:50%;background:var(--green-bright);opacity:.85}
.feature{position:absolute;width:260px}
.feature.left{text-align:right}
.feature h4{font-size:14px;font-weight:600;color:var(--ink);margin-bottom:8px}
.feature p{font-size:10.5px;line-height:19px;color:var(--text)}
.feature-icon{position:absolute;width:34px;height:34px;border-radius:50%;background:#e3ecd7}
.feature-icon::after{content:"";position:absolute;left:9px;top:9px;width:16px;height:16px;border-radius:50%;background:var(--green)}

/* where */
.where-green{position:absolute;top:2220px;left:0;width:1200px;height:460px;background:var(--green)}
.where-media{position:absolute;top:2200px;left:480px;width:720px;height:492px;background:linear-gradient(110deg,rgba(91,154,46,1) 0%,rgba(91,154,46,0) 22%),linear-gradient(180deg,#8fa58a 0%,#4d7a3a 40%,#5d7a54 75%,#8a8f84 100%)}
.where-title{position:absolute;left:122px;top:2274px;font-family:var(--head);font-weight:700;font-size:37px;color:var(--white)}
.where-text{position:absolute;left:122px;top:2332px;width:455px;font-size:10.8px;line-height:18.8px;color:var(--white)}
.where-list{position:absolute;left:136px;top:2462px;font-size:10.5px;line-height:19px;font-weight:600;color:var(--white)}

/* awards */
.badge{position:absolute;top:2831px;width:66px;height:66px;border-radius:50%;border:3px solid #cfcfcf;background:#f3f3f3}
.badge.wide{width:110px;border-radius:10px}

/* blog */
.post{position:absolute;top:3027px;width:307px;height:294px;background:var(--white);box-shadow:0 4px 14px rgba(0,0,0,.1)}
.post-media{position:absolute;left:0;top:0;width:100%;height:211px}
.post-tag{position:absolute;left:3px;top:5px;background:var(--green);color:var(--white);font-size:10px;font-weight:600;padding:4px 7px}
.post h5{position:absolute;left:17px;top:236px;font-size:10.8px;font-weight:600;color:var(--ink)}
.post p{position:absolute;left:17px;top:259px;font-size:10.3px;color:var(--text)}
.post-go{position:absolute;right:12px;top:257px;width:25px;height:25px;border-radius:50%;background:var(--green)}

/* club */
.club{position:absolute;top:3466px;left:0;width:1200px;height:280px;background:linear-gradient(90deg,#3f8e20 0%,#4c9e24 55%,#3b8a1c 100%)}
.club-title{position:absolute;left:122px;top:3532px;font-family:var(--head);font-weight:700;font-size:37px;color:var(--white)}
.club-sub{position:absolute;left:122px;top:3590px;font-size:10.8px;color:var(--white)}
.signup{position:absolute;left:122px;top:3629px;width:540px;height:48px;border:1.5px solid var(--white);border-radius:30px}
.signup span{position:absolute;left:14px;top:15px;font-size:10.5px;color:var(--white)}
.signup .btn{right:3px;top:4px;height:37px;width:98px}
.chips{position:absolute;left:712px;top:3500px;width:488px;height:245px;background:radial-gradient(ellipse at 55% 55%,#f4d36a 0%,#e6b640 40%,rgba(76,158,36,0) 72%)}

/* footer */
.site-footer{position:absolute;top:3745px;left:0;width:1200px;height:276px;background:var(--footer)}
.foot-brand{position:absolute;left:137px;top:3834px;display:flex;flex-direction:column;align-items:center;gap:10px;color:var(--white)}
.foot-brand .dot{width:44px;height:44px;border-radius:50%;background:var(--white)}
.foot-brand b{font-family:var(--head);font-weight:700;font-size:22px;color:var(--white)}
.foot-rule{position:absolute;top:3790px;width:1px;height:170px;background:#3a3a3a}
.foot-head{position:absolute;top:3791px;font-weight:600;font-size:14px;color:var(--white)}
.foot-line{position:absolute;font-size:10.5px;display:flex;align-items:center;gap:10px;color:var(--white)}
.foot-line .ic{width:18px;height:18px;border-radius:50%;background:var(--green-bright)}
.foot-menu{position:absolute;left:760px;top:3831px;font-size:10.5px;line-height:22.6px;color:var(--white)}
.legal{position:absolute;top:3989px;left:0;width:1200px;text-align:center;font-size:10px;color:var(--white)}
</style>
</head>
<body>

<div class="hero-media" role="img" aria-label="Dried banana chips scattered across a dark slate surface"></div>
<svg class="abs" style="left:0;top:610px" width="1200" height="60" viewBox="0 0 1200 60" aria-hidden="true">
  <polygon fill="#ffffff" points="0,40 40,34 70,42 110,30 150,38 200,28 240,36 290,26 330,34 380,30 430,38 480,27 530,35 580,29 630,37 680,26 730,33 780,28 830,37 880,30 930,36 980,27 1030,34 1080,29 1130,37 1170,31 1200,35 1200,60 0,60"/>
</svg>

<header class="site-header">
  <nav class="nav nav-left"><a>Our Snacks</a><a>Our Ingredients</a><a>Our Story</a><a>Where to Buy</a></nav>
  <nav class="nav nav-right"><a>Blog</a><a style="margin-left:10px">Contact</a></nav>
  <span class="account" aria-label="Account"></span>
  <a class="btn btn-solid" style="left:967px;top:8px;width:111px;height:31px;font-size:11px">Find Stockist</a>
</header>
<div class="logo-notch"></div>
<div class="logo-mark" aria-hidden="true"></div>
<div class="logo-name">CRUNCHWELL</div>

<h1 class="hero-title">Rescued Produce. <span class="accent">Real</span><br><span class="accent">Nutrition.</span> Good Energy</h1>
<p class="hero-sub">Wholesome banana-powered snacks, grown locally and crafted to fuel active, healthy lives.</p>
<a class="btn btn-solid" style="left:476px;top:431px;width:116px">Browse Snacks</a>
<a class="btn btn-outline" style="left:604px;top:431px;width:121px;color:var(--green-bright);border-color:var(--green-bright)">Where to Buy →</a>

<div class="deco-mark" aria-hidden="true"></div>
<p class="eyebrow">Community &amp; Growers</p>
<h2 class="intro-title">Good Snacks Start<br>With Good People</h2>
<svg class="abs" style="left:126px;top:874px" width="315" height="16" viewBox="0 0 315 16" aria-hidden="true"><path d="M2 10 Q150 2 312 12" stroke="#5b9a2e" stroke-width="5" fill="none" stroke-linecap="round"/></svg>
<p class="intro-text">Crunchwell is more than just food — it’s a partnership with the Palmera Coast community. Our bananas are grown by local families who care for the land, and every snack is crafted with the knowledge of a horticulturist &amp; a nutritionist. Together, we’re turning local harvests into feel-good energy for active</p>
<a class="btn btn-solid" style="left:572px;top:890px;width:129px">Meet the Growers</a>

<section class="snacks"></section>
<h2 class="section-title" style="top:1035px">Our Snacks</h2>
<span class="arrow-circle" style="left:86px;top:1275px"></span>
<span class="arrow-circle" style="left:1096px;top:1275px"></span>

<article class="card" style="left:122px">
  <div class="card-media" role="img" aria-label="Green snack pouch beside a coconut, apple and bananas"><div class="pack"></div></div>
  <h3>Cocobana Bites</h3>
  <p class="desc">Crunchy banana chips with toasted coconut.</p>
  <p class="tags">Fibre &nbsp;|&nbsp; Potassium &nbsp;|&nbsp; Gluten-Free</p>
  <a class="more">View Product →</a>
</article>
<article class="card" style="left:447px">
  <div class="card-media" role="img" aria-label="Green snack pouch beside a bowl of banana clusters"><div class="pack"></div></div>
  <h3>Banana Chia Crunch</h3>
  <p class="desc">Protein-packed banana clusters with chia seeds.</p>
  <p class="tags">Vegan &nbsp;|&nbsp; Fibre &nbsp;|&nbsp; Omega-3</p>
  <a class="more">View Product →</a>
</article>
<article class="card" style="left:772px">
  <div class="card-media" role="img" aria-label="Green snack pouch beside pieces of dark chocolate"><div class="pack"></div></div>
  <h3>Choco Banana Thins</h3>
  <p class="desc">Palmera bananas dipped in - rich dark choc.</p>
  <p class="tags">Fibre &nbsp;|&nbsp; Antioxidants &nbsp;|&nbsp; Dairy-Free</p>
  <a class="more">View Product →</a>
</article>
<a class="btn btn-solid" style="left:535px;top:1491px;width:130px">View All Product</a>

<h2 class="section-title" style="top:1637px">Why Crunchwell</h2>
<div class="why-emblem" aria-hidden="true"></div>

<span class="feature-icon" style="left:353px;top:1753px"></span>
<div class="feature left" style="left:129px;top:1797px"><h4>Locally Grown</h4><p>Sourced straight from Palmera Bay<br>banana plantations and regional grow-</p></div>
<span class="feature-icon" style="left:353px;top:1950px"></span>
<div class="feature left" style="left:129px;top:1995px"><h4>Functional Nutrition</h4><p>Snacks crafted by a horticulturist + nutri-<br>tionist to fuel active bodies and minds.</p></div>
<span class="feature-icon" style="left:818px;top:1753px"></span>
<div class="feature" style="left:821px;top:1797px"><h4>Community First</h4><p>We support local markets, farmers,<br>and families with every pack we sell.</p></div>
<span class="feature-icon" style="left:818px;top:1950px"></span>
<div class="feature" style="left:821px;top:1995px"><h4>Sustainably Made</h4><p>Eco-conscious production &amp; packag-<br>ing designed with the planet in mind.</p></div>
<a class="btn btn-outline" style="left:526px;top:2110px;width:147px">Discover Our Snacks</a>

<div class="where-green"></div>
<div class="where-media" role="img" aria-label="Aerial view of green hills, banana plantations and a coastal town"></div>
<svg class="abs" style="left:0;top:2196px" width="1200" height="30" viewBox="0 0 1200 30" aria-hidden="true">
  <polygon fill="#ffffff" points="0,0 1200,0 1200,8 1150,14 1100,6 1050,16 1000,9 950,15 900,5 850,13 800,8 750,17 700,7 650,14 600,9 550,18 500,8 450,15 400,10 350,17 300,8 250,14 200,9 150,16 100,7 50,13 0,10"/>
</svg>
<svg class="abs" style="left:0;top:2670px" width="1200" height="30" viewBox="0 0 1200 30" aria-hidden="true">
  <polygon fill="#ffffff" points="0,30 1200,30 1200,22 1150,15 1100,24 1050,12 1000,20 950,13 900,25 850,14 800,21 750,11 700,23 650,15 600,20 550,10 500,22 450,14 400,24 350,12 300,20 250,15 200,25 150,13 100,21 50,14 0,19"/>
</svg>
<h2 class="where-title">Where to Buy</h2>
<p class="where-text">Find us by the beach every Sunday. You can catch Crunchwell in person every week at the Seaside Growers Market — a beautiful makers and growers market held at the Pier Green in Palmera Bay. We bring our full range of handcrafted snacks — from our signature Cocobana to functional favourites like Banoffee and Macabana — all made from upcycled local produce, developed by a grower and a nutritionist who care about what you eat and where it comes from.</p>
<ul class="where-list">
  <li>Seaside Growers Market</li>
  <li>Pier Green, Palmera Bay</li>
  <li>Every Sunday, 8am–2pm</li>
  <li>Beachside, all-weather, all abilities</li>
</ul>
<a class="btn btn-white" style="left:122px;top:2559px;width:168px">Find My Nearest Stockist</a>
<a class="btn btn-ghost" style="left:304px;top:2559px;width:160px">See Market Schedule</a>

<h2 class="section-title" style="top:2752px">Recognised for Quality</h2>
<span class="badge" style="left:180px" aria-label="Award badge"></span>
<span class="badge wide" style="left:340px" aria-label="Certification badge"></span>
<span class="badge" style="left:568px" aria-label="Certification badge"></span>
<span class="badge" style="left:772px" aria-label="Award badge"></span>
<span class="badge" style="left:964px" aria-label="Award badge"></span>

<h2 class="section-title" style="top:2955px">Latest Blog</h2>
<article class="post" style="left:144px">
  <div class="post-media" role="img" aria-label="Hands holding a bowl of banana chips" style="background:linear-gradient(135deg,#e2a52c,#c88a1f 60%,#5a6f82)"></div>
  <span class="post-tag">Grower Stories</span>
  <h5>Meet the Families Behind Palmera Coast Bananas</h5>
  <p>Our snacks start with local growers who...</p>
  <span class="post-go"></span>
</article>
<article class="post" style="left:470px">
  <div class="post-media" role="img" aria-label="Bowl of golden chips with dips on a stone table" style="background:linear-gradient(135deg,#6f7478,#c98a2a 50%,#8a8f93)"></div>
  <span class="post-tag">Nutrition Tips</span>
  <h5>Why Potassium-Packed Snacks Keep You Moving</h5>
  <p>Potassium is key for muscle recovery and...</p>
  <span class="post-go"></span>
</article>
<article class="post" style="left:795px">
  <div class="post-media" role="img" aria-label="Friends sharing snacks at an outdoor market table" style="background:linear-gradient(135deg,#a65a3a,#d9b48c 50%,#5c8a4a)"></div>
  <span class="post-tag">Market Updates</span>
  <h5>Find Us at the Pier Markets Every Sunday</h5>
  <p>Come meet the team, try our newest snacks...</p>
  <span class="post-go"></span>
</article>
<a class="btn btn-solid" style="left:533px;top:3356px;width:134px">Read More Stories</a>

<section class="club"></section>
<svg class="abs" style="left:0;top:3448px" width="1200" height="30" viewBox="0 0 1200 30" aria-hidden="true">
  <polygon fill="#3f8e20" points="0,30 1200,30 1200,12 1160,20 1120,8 1080,18 1040,6 1000,16 960,10 920,20 880,5 840,17 800,9 760,19 720,7 680,16 640,10 600,21 560,8 520,17 480,6 440,18 400,11 360,20 320,7 280,16 240,9 200,19 160,8 120,17 80,10 40,19 0,9"/>
</svg>
<div class="chips" role="img" aria-label="Golden potato chips stacked in a curve"></div>
<h2 class="club-title">Join the Snack Club</h2>
<p class="club-sub">Get seasonal updates, market stall dates, and new snack drops straight from the Palmera Coast.</p>
<div class="signup"><span>Enter Your Email</span><a class="btn btn-white">Subscribe</a></div>

<footer class="site-footer"></footer>
<div class="foot-brand"><span class="dot" aria-hidden="true"></span><b>CRUNCHWELL</b></div>
<span class="foot-rule" style="left:375px"></span>
<span class="foot-rule" style="left:688px"></span>
<span class="foot-rule" style="left:910px"></span>

<p class="foot-head" style="left:448px">Contact Us</p>
<p class="foot-line" style="left:448px;top:3848px"><span class="ic"></span>Palmera Bay, North Coast</p>
<p class="foot-line" style="left:448px;top:3883px;color:var(--green-bright)"><span class="ic"></span>hello@crunchwell-example.au</p>
<p class="foot-line" style="left:448px;top:3919px"><span class="ic"></span>+ 61 2 5550 1842</p>

<p class="foot-head" style="left:760px">Menu</p>
<div class="foot-menu"><p>Our Snacks</p><p>Our Ingredients</p><p>Our Story</p><p>Where to Buy</p><p>Blog</p><p>Contact</p></div>

<p class="foot-head" style="left:996px">Follow Us</p>
<p class="foot-line" style="left:996px;top:3848px"><span class="ic"></span>Chatterbox</p>
<p class="foot-line" style="left:996px;top:3883px"><span class="ic"></span>Quickpost</p>
<p class="foot-line" style="left:996px;top:3919px"><span class="ic"></span>Snapwall</p>

<p class="legal">Twenty Twenty-Five &nbsp;&nbsp;|&nbsp;&nbsp; Privacy Policy &nbsp;&nbsp;|&nbsp;&nbsp; Accessibility Statement &nbsp;&nbsp;|&nbsp;&nbsp; Terms</p>

</body>
</html>
```